Brent Oakes Director / Photographer Branding

I need note pads, envelops, business cards and letter head for my company. I'm a fashion and advertising director / photographer. I'm having trouble deciding how to include both Director & Photographer in my title or if it is even necessary. Maybe just my name is enough. I'm open for even using my initials if it works with the design and overall pieces. Please view my website to see what I have at this moment and what work I do. www.brentoakesstudio-mail.net
Updates

Project Deadline Extended
Reason: Hello Everyone! I'm extending the deadline since I have been traveling on a job out of country and I wanted to have more time to look through all the designs and give enough time for everyone to provide changes with designs and updates. I will be more available to communicate online now that I'm back in the office! Thank you! Brent Oakes

Target Market(s)

Fashion magazines, clothing lines and beauty cosmetic brands.

Industry/Entity Type

Fashion Photography

Font styles to use
Sans Serif

Colors
acd036
acd35d
cbcbcb
f5f5f5

Requirements
Must have
• My name.. Brent Oakes, my website: brentoakesstudio-mail.net my phone number, 555-284-6103
• I don't need my address on these. I also live by the philosophy that less is more and keeping things simple ads strength to a design. I also don't want to stop people from taking chances and experimenting with an idea that might take me down different road with my branding.
Nice to have
• Bold designs and clean lines. I'm open to ideas that I could adopt but I lean towards a more minimalistic look in general.
Should not have
• Not have cheesy graphics or pictures. No images of cameras, film or anything that looks like it is a camera or aperture, lens etc... ;)

```html
<!DOCTYPE html>
<html lang="en">
<head>
<meta charset="utf-8">
<title>Brent Oakes — Stationery</title>
<link href="https://fonts.googleapis.com/css2?family=Raleway:wght@400&display=swap" rel="stylesheet">
<style>
  :root {
    --backdrop: #b4b4b4;
    --paper: #f0f0f0;
    --paper-shade: #e6e6e6;
    --brand-green: #53a600;
    --ghost: rgba(0,0,0,0.045);
    --ink-grey: #8a8a8a;
    --white: #ffffff;
  }
  * { margin: 0; padding: 0; box-sizing: border-box; }
  html, body { width: 1200px; height: 1200px; overflow: hidden; }
  body {
    background: var(--backdrop);
    font-family: "Raleway", sans-serif;
    position: relative;
  }
  .piece {
    position: absolute;
    background: linear-gradient(135deg, var(--paper) 0%, var(--paper) 60%, var(--paper-shade) 100%);
    overflow: hidden;
    box-shadow: 0 1px 3px rgba(0,0,0,0.25);
  }
  .name-label {
    position: absolute;
    font-weight: 400;
    color: var(--brand-green);
    white-space: nowrap;
    line-height: 1;
  }
  .ghost-name {
    position: absolute;
    font-weight: 400;
    color: var(--ghost);
    white-space: nowrap;
    line-height: 1;
  }
  .contact {
    position: absolute;
    color: var(--ink-grey);
    line-height: 1.45;
    white-space: nowrap;
  }
  .accent-bar { position: absolute; background: var(--brand-green); }
  .flap {
    position: absolute;
    background: var(--brand-green);
    color: rgba(255,255,255,0.8);
    font-size: 6.5px;
    text-align: center;
  }

  /* Letterhead */
  .letterhead { left: 106px; top: 108px; width: 454px; height: 588px; }
  .letterhead .name-label { left: 27px; top: 30px; font-size: 20px; }
  .letterhead .ghost-name {
    font-size: 60px;
    left: 392px; top: 568px;
    transform-origin: left top;
    transform: rotate(-90deg);
  }
  .letterhead .accent-bar { left: 0; top: 538px; width: 6px; height: 28px; }
  .letterhead .contact { left: 28px; top: 537px; font-size: 5.4px; }

  /* Envelope, back with flap up */
  .envelope-back-top { left: 616px; top: 132px; width: 504px; height: 226px; }
  .flap-top {
    left: 616px; top: 66px; width: 498px; height: 67px;
    border-radius: 6px 6px 0 0;
  }
  .flap-top .flap-url { display: block; margin-top: 31px; transform: rotate(180deg); }

  .envelope-back-top .name-label,
  .envelope-front .name-label { left: 19px; top: 30px; font-size: 20px; }
  .envelope-ghost { font-size: 60px; left: 14px; bottom: -12px; }

  /* Envelope, open with patterned flap */
  .envelope-open { left: 617px; top: 472px; width: 506px; height: 224px; }
  .flap-open { position: absolute; left: 617px; top: 404px; width: 506px; height: 102px; }

  /* Envelope, front */
  .envelope-front { left: 54px; top: 751px; width: 506px; height: 227px; }

  /* Envelope, back with flap down */
  .envelope-back-bottom { left: 614px; top: 752px; width: 504px; height: 227px; }
  .flap-bottom {
    left: 617px; top: 752px; width: 498px; height: 68px;
    border-radius: 0 0 8px 8px;
    box-shadow: 0 2px 4px rgba(0,0,0,0.2);
  }
  .flap-bottom .flap-url { display: block; margin-top: 30px; }

  /* Business cards */
  .card-front { left: 366px; top: 1028px; width: 194px; height: 108px; }
  .card-front .accent-bar { left: 0; top: 74px; width: 5px; height: 20px; }
  .card-front .contact { left: 15px; top: 74px; font-size: 4.4px; }
  .card-front .name-label { right: 12px; top: 84px; font-size: 11px; }

  .card-back {
    left: 615px; top: 1028px; width: 194px; height: 108px;
    background: var(--brand-green);
  }
  .card-back .name-label { color: var(--white); left: 13px; top: 66px; font-size: 15px; }
  .card-back .card-url {
    position: absolute; left: 14px; top: 88px;
    font-size: 4.4px; color: rgba(255,255,255,0.85);
  }
</style>
</head>
<body>

  <section class="piece letterhead">
    <div class="name-label">Brent Oakes</div>
    <div class="ghost-name">Brent Oakes</div>
    <div class="accent-bar"></div>
    <div class="contact">
      Brent Oakes Photographer<br>
      555-284-6103<br>
      brent@brentoakesstudio-mail.net<br>
      www.brentoakesstudio-mail.net
    </div>
  </section>

  <div class="flap flap-top"><span class="flap-url">www.brentoakesstudio-mail.net</span></div>
  <section class="piece envelope-back-top">
    <div class="name-label">Brent Oakes</div>
    <div class="ghost-name envelope-ghost">Brent Oakes</div>
  </section>

  <section class="piece envelope-open"></section>
  <svg class="flap-open" viewBox="0 0 506 102" role="img" aria-label="Green inner flap with repeated name pattern">
    <path d="M4,10 Q4,0 16,0 H490 Q502,0 502,10 V86 Q492,80 484,90 L476,102 H48 Q38,86 24,82 Q8,80 0,88 Z" fill="#53a600"/>
  </svg>

  <section class="piece envelope-front">
    <div class="name-label">Brent Oakes</div>
    <div class="ghost-name envelope-ghost">Brent Oakes</div>
  </section>

  <section class="piece envelope-back-bottom"></section>
  <div class="flap flap-bottom"><span class="flap-url">www.brentoakesstudio-mail.net</span></div>

  <section class="piece card-front">
    <div class="accent-bar"></div>
    <div class="contact">
      Photographer | Director<br>
      555-284-6103<br>
      brent@brentoakesstudio-mail.net<br>
      www.brentoakesstudio-mail.net
    </div>
    <div class="name-label">Brent Oakes</div>
  </section>

  <section class="piece card-back">
    <div class="name-label">Brent Oakes</div>
    <div class="card-url">www.brentoakesstudio-mail.net</div>
  </section>

</body>
</html>
```